Exciting, Bold and Modern Landscaping & Turf care company business card

Hello, I own a lawn and landscaping company in Virginia, USA. We would like to design a bold, dynamic, modern business card that really makes us stand out. I tire of all green business cards with crappy, cartoonish clipart grass on them. It needs to be two sided, on one side i need to highlight our turf care division called "Promised Brighter Meadow" We maintain grass, fertilize it, weed control, etc.. We have a green thumbed gopher as our logo that i will attach. I am looking for something, clean and neat but out of the box in style. Im open to all ideas, and would like different options for them. On the other side, i want to highlight our landscaping division "Quiet Harbor Landscaping" In this division we design and install landscapes. Feel free to visit our website for more info or email me with ANY questions. Our busines cards in the past have highlighted our different services, but i don't want to this time. By the time I hand out a business card we are usually already estimating a project and they know what services we offer. I do want them to look at my card and say "wow thats pretty cool" and for them to think "These guys are something different, not just your standard dirt diggers" The logo doesnt have to be on both sides, but it needs to be on the turf care side. Our phone number and website should also be on at least on side, but need not be on both. The phone number is (555)618-4072 as well as the web address as www.MossbrookYardWorks.example. I like for the web address to have caps like that becasue it makes the long address much easier to read. I would like it in full color, printing costs are not my major concern. I also love rounded corners or interesting die cut designs as well, so feel free to wow me. Whether it be a clean white background with a bold photo to an all black card with a gray logo except for his green thumb with silver foil lettering to anything in between, lets go for it. That bieng said i dont want anything cartoonish, we are still a professional service and i want that to come through. THANKS!
Updates
Project Deadline Extended
Reason: changed project to a committed payment. I would like designers to re-evaluate their interest now and give them extra time to submit designs. Thank you.
we have changed our status to a commited payment to entice more submissions. thank you all for your hard work!
Industry/Entity Type
Professional Service
Look and feel
Each slider illustrates characteristics of the customer's brand and the style your logo design should communicate.

```html
<!DOCTYPE html>
<html lang="en">
<head>
<meta charset="utf-8">
<title>Mossbrook Yard Works – Business Card</title>
<link rel="stylesheet" href="https://fonts.googleapis.com/css2?family=Source+Sans+3:wght@400;600;700&display=swap">
<style>
  :root {
    --backdrop: #e9ebe8;
    --green-deep: #0d4a06;
    --green-mid: #1f8a10;
    --green-bright: #4fc41c;
    --ray-light: rgba(235, 255, 200, 0.55);
    --accent-orange: #f39a12;
    --text-white: #ffffff;
    --mark-circle: #ffffff;
  }
  * { margin: 0; padding: 0; box-sizing: border-box; }
  html, body {
    width: 1200px;
    height: 900px;
    overflow: hidden;
    background: var(--backdrop);
    font-family: "Source Sans 3", "Myriad Pro", sans-serif;
  }
  .canvas {
    position: relative;
    width: 1200px;
    height: 900px;
  }
  .card {
    position: absolute;
    top: 290px;
    width: 540px;
    height: 330px;
    border-radius: 28px;
    overflow: hidden;
    background:
      radial-gradient(ellipse 55% 70% at 50% 0%, var(--ray-light), transparent 70%),
      repeating-conic-gradient(from 150deg at 50% -10%, rgba(255,255,255,0.16) 0deg 3deg, transparent 3deg 9deg),
      radial-gradient(ellipse 90% 110% at 50% 10%, var(--green-bright) 0%, var(--green-mid) 45%, var(--green-deep) 100%);
  }
  .card--turf { left: 60px; }
  .card--landscape { left: 630px; }

  /* Turf side: brand mark */
  .brand-mark {
    position: absolute;
    left: 0;
    right: 0;
    top: 38px;
    display: flex;
    flex-direction: column;
    align-items: center;
    gap: 18px;
  }
  .brand-mark__circle {
    width: 196px;
    height: 196px;
    border-radius: 50%;
    background: var(--mark-circle);
  }
  .brand-mark__name {
    font-weight: 700;
    font-size: 28px;
    color: var(--accent-orange);
    letter-spacing: 0.2px;
  }

  /* Landscape side: divisions & contact */
  .divisions {
    position: absolute;
    right: 34px;
    top: 118px;
    text-align: right;
  }
  .divisions__primary {
    font-weight: 700;
    font-size: 28px;
    line-height: 34px;
    color: var(--text-white);
  }
  .divisions__primary .amp { font-weight: 400; }
  .divisions__secondary {
    font-weight: 700;
    font-size: 28px;
    line-height: 34px;
    color: var(--accent-orange);
    margin-right: 88px;
  }
  .divisions__parent {
    font-size: 13px;
    font-weight: 400;
    color: var(--text-white);
    margin-top: 2px;
  }
  .contact {
    position: absolute;
    left: 0;
    right: 0;
    top: 243px;
    text-align: center;
    padding-left: 10px;
  }
  .contact__phone {
    font-size: 23px;
    font-weight: 400;
    color: var(--text-white);
    line-height: 28px;
  }
  .contact__web {
    font-size: 15px;
    font-weight: 400;
    color: var(--accent-orange);
    line-height: 20px;
  }
</style>
</head>
<body>
<main class="canvas">
  <section class="card card--turf">
    <div class="brand-mark">
      <div class="brand-mark__circle"></div>
      <div class="brand-mark__name">Mossbrook Yard Works</div>
    </div>
  </section>

  <section class="card card--landscape">
    <div class="divisions">
      <p class="divisions__primary">Quiet Harbor Landscaping <span class="amp">&amp;</span></p>
      <p class="divisions__secondary">Promised Brighter Meadow</p>
      <p class="divisions__parent">Divisions of Tidewell Ventures, Inc.</p>
    </div>
    <div class="contact">
      <p class="contact__phone">(555) 618-4072</p>
      <p class="contact__web">www.MossbrookYardWorks.example</p>
    </div>
  </section>
</main>
</body>
</html>
```